Review/Re-Design Supermarket E-Commerce website

We have launched our Supermarket E-commerce Website but feel it is lacking a modern feel.

Please re-design the current Supermarket E-commerce site, creating a more modern look and feel.

I am looking for design changes to things such as:

- Fonts
- Button shape & Size
- Shapes of boxes
- Layout of drop down menus
- A new shopping cart / button
- The Header (and in particular the use and positioning of the logo)
- Supplying a generic background image (currently berries)

Please do not change the structure of the page. For instance, the category selection will always be on the left, the items will always be displayed in rows of 3 and the shopping cart should be on the right.
Updates

Current site can be found at www.korvamarketplace.com.au

Project Deadline Extended
Reason: designs coming in are generally too different from current design. we are looking for less that 10% change to the overall look and feel. one aspect that needs a lot of work is the checkout cart on the right hand side. please checkout http://www2.pellingtonfresh.com.au/?gclid=XQWB4pzrhnLDGAKUrTmeYbNVsP

Target Market(s)

Consumers buying their weekly grocery shopping online

Industry/Entity Type

Shopping

Number of Pages Required

1 page

Requirements
Must have
• Stick to the branding of the Logo. Which is Red, Blue and White.
• Other colours may be used in small percentages.
Should not have
• Do not change the Structure of the site.

```html
<!DOCTYPE html>
<html lang="en">
<head>
<meta charset="utf-8">
<title>Harbourline Fresh Supermarkets – Apples</title>
<link rel="stylesheet" href="https://fonts.googleapis.com/css2?family=Exo+2:wght@400;500;600&display=swap">
<style>
:root{
  --red:#e30b0b;
  --red-dark:#b80707;
  --black:#111111;
  --footer:#262626;
  --footer-line:#4a4a4a;
  --grey-band:#c9c9c9;
  --side-a:#cbcbcb;
  --side-b:#bdbdbd;
  --white:#ffffff;
  --text:#1a1a1a;
  --footer-text:#e9e9e9;
  --muted:#9a9a9a;
}
*{box-sizing:border-box;margin:0;padding:0}
html,body{width:1121px;height:1200px;overflow:hidden}
body{font-family:"Exo 2",sans-serif;color:var(--text);position:relative;background:#5a5a5a}
a{color:inherit;text-decoration:none}
.backdrop{position:absolute;inset:0;background:
  radial-gradient(circle at 4% 25%,#c4191b 0,#8a0c0e 12%,transparent 20%),
  radial-gradient(circle at 97% 40%,#c4191b 0,#8a0c0e 12%,transparent 20%),
  radial-gradient(circle at 3% 85%,#b81416 0,#7a0a0c 12%,transparent 20%),
  radial-gradient(circle at 98% 90%,#b81416 0,#7a0a0c 12%,transparent 20%),
  linear-gradient(180deg,#6a6a6a,#4c4c4c)}
.page{position:absolute;left:69px;top:10px;width:982px;height:1190px}
.brand{position:absolute;left:0;top:0;width:351px;height:130px;background:var(--red);display:flex;align-items:flex-end;padding:0 18px 22px}
.brand-name{color:var(--white);font-weight:600;font-size:21px;line-height:1.05;letter-spacing:.3px}
.topbar{position:absolute;left:351px;top:0;width:631px;height:57px;background:var(--black);color:var(--white)}
.phone{position:absolute;left:20px;top:8px;display:flex;align-items:center;gap:8px;font-size:32px}
.account{position:absolute;right:6px;top:24px;display:flex;gap:30px;font-size:14px}
.account .current{color:var(--red);text-decoration:underline}
.navband{position:absolute;left:351px;top:57px;width:631px;height:73px;background:var(--grey-band)}
.crumbs{position:absolute;left:16px;top:25px;display:flex;align-items:center;font-size:18px}
.crumbs a{padding:0 9px}
.crumbs .home{background:var(--red);color:var(--white);height:48px;line-height:48px;padding:0 16px;margin-right:9px}
.select{position:absolute;top:44px;height:28px;border:2px solid var(--red);background:#bdbdbd;font-size:13px;display:flex;align-items:center;justify-content:center;gap:6px}
.filter{left:339px;width:85px}
.sort{left:433px;width:85px}
.search{position:absolute;left:528px;top:38px;width:172px;height:35px;display:flex}
.search-field{flex:1;background:#6d6d6d;color:var(--white);font-size:10px;padding:13px 8px 0}
.search-btn{width:31px;background:var(--red);display:flex;align-items:center;justify-content:center}
.content{position:absolute;left:0;top:130px;width:982px;height:744px;background:
  radial-gradient(ellipse at 70% 45%,#e7a7a7 0,transparent 45%),
  radial-gradient(ellipse at 40% 20%,#d99a9a 0,transparent 40%),
  linear-gradient(180deg,#d6d6d6,#c4c4c4)}
.categories{position:absolute;left:0;top:12px;width:203px}
.categories h2{height:48px;background:var(--red);font-size:18px;font-weight:500;text-align:center;line-height:48px;letter-spacing:.5px}
.categories li{list-style:none;height:48px;line-height:48px;text-align:center;font-size:17px;background:var(--side-a)}
.categories li:nth-child(even){background:var(--side-b)}
.products{position:absolute;left:213px;top:12px;display:grid;grid-template-columns:repeat(3,203px);grid-auto-rows:224px;column-gap:9px;row-gap:14px}
.card{background:var(--white);position:relative;text-align:center}
.card.active{outline:2px solid var(--red);outline-offset:-2px}
.card-photo{position:absolute;left:46px;top:6px;width:110px;height:100px;border-radius:40% 40% 50% 50%;background:radial-gradient(circle at 50% 38%,#ea5a2c 0,#d8421f 35%,#c9a474 62%,#fff 72%)}
.card-title{position:absolute;left:0;right:0;top:111px;font-size:17px}
.qty{position:absolute;left:112px;top:160px;display:flex;align-items:center;gap:6px;font-size:17px}
.qty i{width:11px;height:11px;border-radius:50%;background:var(--black);display:inline-block;position:relative}
.qty i::after{content:"";position:absolute;left:3px;top:5px;width:5px;height:1px;background:var(--red)}
.buy{position:absolute;left:37px;top:182px;height:34px;display:flex;gap:2px}
.buy .cart{width:40px;background:var(--black);display:flex;align-items:center;justify-content:center}
.buy .price{width:79px;background:var(--black);color:var(--white);font-size:20px;line-height:34px}
.active .buy .cart,.active .buy .price{background:var(--red)}
.footer{position:absolute;left:0;top:864px;width:982px;height:276px;background:var(--footer);color:var(--footer-text);font-size:15px}
.col{position:absolute;top:0;height:276px;padding-top:24px}
.col+.col{border-left:1px solid var(--footer-line)}
.col li{list-style:none;line-height:26px}
.col-app{left:0;width:287px}
.col-app h3{font-weight:400;font-size:15px;position:absolute;left:28px;top:24px}
.store-badge{position:absolute;left:31px;top:69px;width:131px;height:44px;background:#000;border:1px solid #555;border-radius:4px}
.mobile-badge{position:absolute;left:32px;top:119px;width:129px;height:44px;background:var(--white);border-radius:5px;color:#222;font-size:12px;line-height:13px;display:flex;align-items:center;gap:8px;padding-left:12px}
.accept{position:absolute;left:50px;top:176px;font-size:20px}
.cards{position:absolute;left:9px;top:224px;display:flex;gap:7px}
.cards span{width:44px;height:28px;background:#d8d8d8;border-radius:3px}
.col-a{left:287px;width:190px;padding-left:11px}
.col-b{left:477px;width:167px;padding-left:11px}
.col-c{left:644px;width:166px;padding-left:11px;padding-top:20px}
.col-d{left:810px;width:172px;padding-left:12px;padding-top:20px}
.social{display:flex;gap:12px;margin-top:6px}
.social span{width:38px;height:38px;border-radius:50%;background:var(--red)}
.copyright{position:absolute;left:0;top:1140px;width:982px;height:50px;background:#000;color:var(--muted);font-size:15px;text-align:center;line-height:46px}
</style>
</head>
<body>
<div class="backdrop" role="img" aria-label="Background photograph of red apples on a grey surface"></div>
<div class="page">
  <header>
    <div class="brand"><span class="brand-name">HARBOURLINE FRESH<br>SUPERMARKETS</span></div>
    <div class="topbar">
      <div class="phone">
        <svg width="24" height="24" viewBox="0 0 24 24"><circle cx="12" cy="12" r="12" fill="#e30b0b"/><path d="M8 6l2.5 0 1 3-1.6 1.2a8 8 0 0 0 3.9 3.9L15 12.5l3 1V16a1.5 1.5 0 0 1-1.6 1.5A11 11 0 0 1 6.5 7.6 1.5 1.5 0 0 1 8 6z" fill="#111"/></svg>
        1300 555 208
      </div>
      <nav class="account"><a class="current" href="#">Products</a><a href="#">login</a><a href="#">Register</a></nav>
    </div>
    <div class="navband">
      <nav class="crumbs"><a class="home" href="#">Home</a><a href="#">Fruit</a><a href="#">Apples</a></nav>
      <div class="select filter">Filter By <span>&#9662;</span></div>
      <div class="select sort">Sort <span>&#9662;</span></div>
      <div class="search">
        <div class="search-field">Search</div>
        <div class="search-btn"><svg width="22" height="22" viewBox="0 0 22 22"><circle cx="9" cy="9" r="6.5" fill="none" stroke="#111" stroke-width="2.5"/><path d="M14 14l6 6" stroke="#111" stroke-width="3" stroke-linecap="round"/></svg></div>
      </div>
    </div>
  </header>

  <main class="content" role="img" aria-label="Soft blurred photograph of red apples behind the product area">
    <aside class="categories">
      <h2>ONLINE SPECIALS</h2>
      <ul>
        <li>baby</li><li>bakery</li><li>baking needs</li><li>coconut</li><li>coffee</li><li>cordials</li><li>energy drinks</li><li>flavoured waters</li><li>fruit drink</li><li>iced tea</li><li>long life juice</li><li>powdered milk &amp; flav.</li><li>soda water</li>
      </ul>
    </aside>
    <section class="products">
      <article class="card active"><div class="card-photo" role="img" aria-label="Basket of red apples"></div><h3 class="card-title">apples red 2kg bag</h3><div class="qty"><i></i>1<i></i></div><div class="buy"><span class="cart"><svg width="26" height="22" viewBox="0 0 26 22"><path d="M1 2h4l3 12h13l3-9H7" fill="none" stroke="#fff" stroke-width="2.4" stroke-linejoin="round"/><circle cx="10" cy="19" r="2" fill="#fff"/><circle cx="19" cy="19" r="2" fill="#fff"/></svg></span><span class="price">$8.39</span></div></article>
      <article class="card"><div class="card-photo" role="img" aria-label="Basket of red apples"></div><h3 class="card-title">apples red 2kg bag</h3><div class="qty"><i></i>1<i></i></div><div class="buy"><span class="cart"><svg width="26" height="22" viewBox="0 0 26 22"><path d="M1 2h4l3 12h13l3-9H7" fill="none" stroke="#fff" stroke-width="2.4" stroke-linejoin="round"/><circle cx="10" cy="19" r="2" fill="#fff"/><circle cx="19" cy="19" r="2" fill="#fff"/></svg></span><span class="price">$8.39</span></div></article>
      <article class="card"><div class="card-photo" role="img" aria-label="Basket of red apples"></div><h3 class="card-title">apples red 2kg bag</h3><div class="qty"><i></i>1<i></i></div><div class="buy"><span class="cart"><svg width="26" height="22" viewBox="0 0 26 22"><path d="M1 2h4l3 12h13l3-9H7" fill="none" stroke="#fff" stroke-width="2.4" stroke-linejoin="round"/><circle cx="10" cy="19" r="2" fill="#fff"/><circle cx="19" cy="19" r="2" fill="#fff"/></svg></span><span class="price">$8.39</span></div></article>
      <article class="card"><div class="card-photo" role="img" aria-label="Basket of red apples"></div><h3 class="card-title">apples red 2kg bag</h3><div class="qty"><i></i>1<i></i></div><div class="buy"><span class="cart"><svg width="26" height="22" viewBox="0 0 26 22"><path d="M1 2h4l3 12h13l3-9H7" fill="none" stroke="#fff" stroke-width="2.4" stroke-linejoin="round"/><circle cx="10" cy="19" r="2" fill="#fff"/><circle cx="19" cy="19" r="2" fill="#fff"/></svg></span><span class="price">$8.39</span></div></article>
      <article class="card"><div class="card-photo" role="img" aria-label="Basket of red apples"></div><h3 class="card-title">apples red 2kg bag</h3><div class="qty"><i></i>1<i></i></div><div class="buy"><span class="cart"><svg width="26" height="22" viewBox="0 0 26 22"><path d="M1 2h4l3 12h13l3-9H7" fill="none" stroke="#fff" stroke-width="2.4" stroke-linejoin="round"/><circle cx="10" cy="19" r="2" fill="#fff"/><circle cx="19" cy="19" r="2" fill="#fff"/></svg></span><span class="price">$8.39</span></div></article>
      <article class="card"><div class="card-photo" role="img" aria-label="Basket of red apples"></div><h3 class="card-title">apples red 2kg bag</h3><div class="qty"><i></i>1<i></i></div><div class="buy"><span class="cart"><svg width="26" height="22" viewBox="0 0 26 22"><path d="M1 2h4l3 12h13l3-9H7" fill="none" stroke="#fff" stroke-width="2.4" stroke-linejoin="round"/><circle cx="10" cy="19" r="2" fill="#fff"/><circle cx="19" cy="19" r="2" fill="#fff"/></svg></span><span class="price">$8.39</span></div></article>
      <article class="card"><div class="card-photo" role="img" aria-label="Basket of red apples"></div><h3 class="card-title">apples red 2kg bag</h3><div class="qty"><i></i>1<i></i></div><div class="buy"><span class="cart"><svg width="26" height="22" viewBox="0 0 26 22"><path d="M1 2h4l3 12h13l3-9H7" fill="none" stroke="#fff" stroke-width="2.4" stroke-linejoin="round"/><circle cx="10" cy="19" r="2" fill="#fff"/><circle cx="19" cy="19" r="2" fill="#fff"/></svg></span><span class="price">$8.39</span></div></article>
      <article class="card"><div class="card-photo" role="img" aria-label="Basket of red apples"></div><h3 class="card-title">apples red 2kg bag</h3><div class="qty"><i></i>1<i></i></div><div class="buy"><span class="cart"><svg width="26" height="22" viewBox="0 0 26 22"><path d="M1 2h4l3 12h13l3-9H7" fill="none" stroke="#fff" stroke-width="2.4" stroke-linejoin="round"/><circle cx="10" cy="19" r="2" fill="#fff"/><circle cx="19" cy="19" r="2" fill="#fff"/></svg></span><span class="price">$8.39</span></div></article>
      <article class="card"><div class="card-photo" role="img" aria-label="Basket of red apples"></div><h3 class="card-title">apples red 2kg bag</h3><div class="qty"><i></i>1<i></i></div><div class="buy"><span class="cart"><svg width="26" height="22" viewBox="0 0 26 22"><path d="M1 2h4l3 12h13l3-9H7" fill="none" stroke="#fff" stroke-width="2.4" stroke-linejoin="round"/><circle cx="10" cy="19" r="2" fill="#fff"/><circle cx="19" cy="19" r="2" fill="#fff"/></svg></span><span class="price">$8.39</span></div></article>
    </section>
  </main>

  <footer class="footer">
    <div class="col col-app">
      <h3>Download Our App</h3>
      <span class="store-badge" aria-label="App store badge"></span>
      <span class="mobile-badge"><svg width="12" height="22" viewBox="0 0 12 22"><rect x="1" y="1" width="10" height="20" rx="2" fill="none" stroke="#222" stroke-width="1.6"/></svg>Mobile site<br>Available</span>
      <p class="accept">We accept</p>
      <div class="cards" aria-label="Accepted payment methods"><span></span><span></span><span></span><span></span><span></span></div>
    </div>
    <ul class="col col-a"><li>My Account</li><li>My Past Orders</li><li>Online Specials</li><li>Everyday Specials</li><li>About QuickLane</li><li>About Us</li></ul>
    <ul class="col col-b"><li>Delivery</li><li>FAQ</li><li>Privacy Policy</li><li>Terms &amp; Conditions</li><li>Contact us</li><li>1300 555 208</li></ul>
    <ul class="col col-c"><li>End User License</li><li>Agreement</li></ul>
    <div class="col col-d"><p>Follow Us On:-</p><div class="social"><span></span><span></span><span></span></div></div>
  </footer>
  <p class="copyright">© QuickLane Pty Ltd 2014 - All Rights Reserved</p>
</div>
</body>
</html>
```